Need UI Design for HRIS/Company Employee Portal

Currently have a custom built system that we hire and use as our employee database and employee portal for everyone in our company. The software has evolved dramatically and needs to be completely user friendly and aesthetically pleasing. Attached are a few ideas and pages we already have. Please make 5 designs for the 5 different pages below. Would need all specifications of content used, color code, font/typography, icons used, etc. We can pretty much pull any information from anywhere we have for example, employee photo, address, DOB, Hire date, Title, ETC.

-Company Staff/Admin Welcome Page
- We want quick shortcuts/buttons or icons for staff functions, such as terminate, hire, information change, reports, etc
-Employee Profile Welcome Page
- We want quick shortcuts/buttons or icons for direct deposit, time off request, information change, pay stubs
-List of Applications/Candidates Page
-Profile Search Page
-Manage Inventory

Target Market(s)

Employees

Industry/Entity Type

It Company

Coding

Coded - Design and coding required

Number of Pages Required

5+ page

Font styles to use
Sans Serif

Requirements
Must have
• Must be professional! Aesthetics, Icons, Easy User Interface, Modern New technology look, can be responsive to mobile
Should not have
• Nothing old school

```html
<!DOCTYPE html>
<html lang="en">
<head>
<meta charset="utf-8">
<title>Employee Profile</title>
<link href="https://fonts.googleapis.com/css2?family=Lato:ital,wght@0,400;0,700;1,400&display=swap" rel="stylesheet">
<style>
:root{
  --bg:#f0f0f0;--white:#fff;--ink:#333;--muted:#666;--line:#e4e4e4;
  --side:#2f3038;--side-top:#27282e;--side-line:#45464e;
  --teal:#22b8a9;--teal-d:#1a9e91;
  --orange:#fa8660;--orange-d:#f26c43;
  --green:#acc97b;--green-d:#8bb04e;
  --yellow:#f3dc6b;--yellow-d:#efc71f;
  --blue:#56cff1;--blue-d:#31bde6;
  --dark:#2e2f37;--dark-d:#24252b;
  --footer:#f1db6b;--pink:#fdeee8;--sky:#eaf8fc;
}
*{margin:0;padding:0;box-sizing:border-box}
html,body{width:1200px;height:899px;overflow:hidden;background:var(--bg)}
body{font-family:'Lato',sans-serif;color:var(--ink)}
.stage{position:absolute;left:0;top:0;width:1280px;height:959px;transform:scale(.9375);transform-origin:0 0;background:var(--bg)}
.abs{position:absolute}
.topbar{left:0;top:0;width:1280px;height:98px;background:var(--white);box-shadow:0 2px 4px rgba(0,0,0,.08)}
.brand{left:55px;top:28px;display:flex;align-items:center;gap:12px;font-size:16px;font-weight:700;color:#2a3f8f}
.brand-mark{width:40px;height:40px;background:#2a3f8f;border-radius:50%}
.search{left:362px;top:36px;width:473px;height:33px;border-bottom:1px solid #e6e6e6}
.tool{width:34px;height:34px;background:#ececec;top:34px;display:flex;align-items:center;justify-content:center}
.badge{position:absolute;top:-9px;right:-9px;width:18px;height:18px;border-radius:50%;color:#fff;font-size:11px;display:flex;align-items:center;justify-content:center}
.vdiv{top:34px;width:1px;height:34px;background:#e2e2e2}
.user-photo{left:1073px;top:23px;width:50px;height:50px;border-radius:50%;background:linear-gradient(#8a9bb0,#3b4555)}
.user-name{left:1142px;top:40px;font-size:15px;font-weight:700;color:#666}
.sidebar{left:55px;top:98px;width:291px;height:804px;background:var(--side)}
.side-top{left:0;top:0;width:291px;height:114px;background:var(--side-top)}
.profile-photo{left:74px;top:48px;width:130px;height:130px;border-radius:50%;border:5px solid #fff;background:linear-gradient(#cfd8df,#7f8d99)}
.status{left:0;width:291px;text-align:center;color:#d8d8d8}
.facts{left:0;top:291px;width:291px;list-style:none}
.facts li{height:40px;border-bottom:2px solid var(--side-line);display:flex;align-items:center;font-size:15px;color:#cfcfcf;padding-left:13px}
.facts li:first-child{border-top:2px solid var(--side-line)}
.facts .k{width:144px}.facts .v{color:#fff;font-weight:700;margin-left:7px}
.btn{display:flex;align-items:center;height:68px;color:#fff;font-size:26px}
.btn .ic{width:62px;height:100%;display:flex;align-items:center;justify-content:center;margin-right:14px}
.card{background:var(--white);box-shadow:0 1px 3px rgba(0,0,0,.1)}
.nav{left:364px;top:112px;width:860px;height:46px;display:flex;align-items:center;padding-left:16px;font-size:15px;color:#555}
.nav span.sep{color:#bbb;margin:0 16px}
.info-head{left:365px;top:177px;width:545px;height:46px;font-size:25px;font-weight:700;color:#555;padding:7px 20px}
.info{left:365px;top:235px;width:545px;height:246px}
.row{position:absolute;height:40px;display:flex;align-items:center;font-size:15px;border-bottom:1px solid var(--line)}
.row .sq{width:30px;height:30px;margin-right:8px;display:flex;align-items:center;justify-content:center;border-right:1px solid var(--line)}
.row .lab{color:#666;margin:0 8px 0 7px}.row b{font-weight:700;color:#333}
.cal{left:930px;top:177px;width:294px;height:304px}
.cal-head{height:46px;border-bottom:1px solid var(--line);display:flex;align-items:center;padding-left:7px;font-size:16px;font-weight:700;color:#555}
.cal-head .sq{width:34px;height:34px;background:var(--teal);margin-right:20px;display:flex;align-items:center;justify-content:center}
.dow{position:absolute;top:53px;width:34px;text-align:center;font-size:14px;color:#777}
.day{position:absolute;width:34px;height:34px;background:#ededed;border:1px solid #dedede;font-size:14px;color:#888;display:flex;align-items:center;justify-content:center}
.day.sun{background:var(--pink);color:#f08a64}.day.today{background:var(--sky)}
.msg{top:502px;width:263px;height:267px}
.msg-head{height:50px;border-bottom:1px solid var(--line);display:flex;align-items:center;padding-left:8px;font-size:16px;font-weight:700;color:#555}
.msg-head .sq{width:34px;height:34px;margin-right:8px;display:flex;align-items:center;justify-content:center}
.msg p{padding:20px 18px 0 19px;font-style:italic;font-size:16px;line-height:25.6px;letter-spacing:.7px;color:#777}
.q{font-size:44px;color:#ccc;font-style:normal;font-weight:700;line-height:0;vertical-align:-14px}
.footer{left:0;top:902px;width:1280px;height:57px;background:var(--footer);display:flex;align-items:center;justify-content:center;font-size:15px;color:#444;padding-left:50px}
</style>
</head>
<body>
<div class="stage">
  <header class="abs topbar">
    <div class="abs brand"><span class="brand-mark"></span>SENTINEL SHIELD SERVICES, INC.</div>
    <div class="abs search"><svg width="20" height="20" viewBox="0 0 20 20" style="margin:5px 0 0 7px"><circle cx="8" cy="8" r="6" fill="none" stroke="#ccc" stroke-width="2.5"/><path d="M12.5 12.5l5 5" stroke="#ccc" stroke-width="3"/></svg></div>
    <div class="abs tool" style="left:861px"><svg width="20" height="14"><rect width="20" height="14" fill="#c9c9c9"/><path d="M0 0l10 8 10-8" stroke="#fff" fill="none" stroke-width="1.5"/></svg><span class="badge" style="background:var(--blue)">5</span></div>
    <div class="abs vdiv" style="left:912px"></div>
    <div class="abs tool" style="left:931px"><svg width="18" height="20"><path d="M9 1c-4 0-6 3-6 7v5l-2 3h16l-2-3V8c0-4-2-7-6-7z" fill="#c9c9c9"/><circle cx="9" cy="18" r="2" fill="#c9c9c9"/></svg><span class="badge" style="background:var(--orange)">2</span></div>
    <div class="abs vdiv" style="left:981px"></div>
    <div class="abs tool" style="left:997px"><svg width="22" height="22"><path d="M6 5a8 8 0 1 0 10 0" fill="none" stroke="#c9c9c9" stroke-width="2.5"/><path d="M11 2v9" stroke="#c9c9c9" stroke-width="2.5"/></svg></div>
    <div class="abs vdiv" style="left:1047px"></div>
    <div class="abs user-photo" role="img" aria-label="Photo of signed-in user"></div>
    <div class="abs user-name">Daniel Ward</div>
  </header>

  <aside class="abs sidebar">
    <div class="abs side-top"></div>
    <div class="abs profile-photo" role="img" aria-label="Employee portrait photo"></div>
    <div class="abs status" style="top:194px;font-size:20px;font-weight:700">Status</div>
    <div class="abs status" style="top:224px;font-size:16px">Hire date 8/1/2000</div>
    <div class="abs status" style="top:245px;font-size:16px">17 years</div>
    <ul class="abs facts">
      <li><span class="k" style="padding-left:3px">DOB</span>:<span class="v">3/12/1986</span></li>
      <li><span class="k">Guard Card Number</span>:<span class="v">skod145DS4</span></li>
      <li><span class="k">Guard Card Expiry</span>:<span class="v">8/1/2030</span></li>
      <li><span class="k">SSN</span>:<span class="v">1688</span></li>
      <li><span class="k">Twic Card Number</span>:<span class="v">2683268</span></li>
      <li><span class="k">ID Document Type</span>:<span class="v">sd2498335</span></li>
      <li><span class="k">ID Document Expiry</span>:<span class="v">1686ad833</span></li>
      <li><span class="k">Report To</span>:<span class="v">Phoenix, AZ</span></li>
    </ul>
    <a class="abs btn" style="left:14px;top:699px;width:263px;background:var(--teal)"><span class="ic" style="background:var(--teal-d)"><svg width="34" height="34"><path d="M4 3h16v8M4 3v28h10" fill="none" stroke="#fff" stroke-width="3"/><path d="M14 29l14-14 4 4-14 14h-4z" fill="#fff"/></svg></span>Edit Profile</a>
  </aside>

  <nav class="abs card nav">Home<span class="sep">|</span>Personal Licenses<span class="sep">|</span>Forms\ Requests<span class="sep">|</span>Team Contacts<span class="sep">|</span>Benifits<span class="sep">|</span>Training<span class="sep">|</span>Equipment<span class="sep">|</span>Help</nav>

  <div class="abs card info-head">Information</div>
  <section class="abs card info">
    <div class="row" style="left:19px;top:8px;width:506px"><span class="sq"><svg width="30" height="30"><rect width="30" height="30" fill="var(--orange)"/><circle cx="15" cy="11" r="5" fill="#fff"/><path d="M6 24c1-6 5-8 9-8s8 2 9 8z" fill="#fff"/></svg></span><span class="lab">Name :</span><b>Marcus Ellery</b></div>
    <div class="row" style="left:19px;top:48px;width:506px"><span class="sq"><svg width="30" height="30"><rect width="30" height="30" fill="var(--teal)"/><path d="M15 24s-6-7-6-11a6 6 0 0 1 12 0c0 4-6 11-6 11z" fill="#fff"/><circle cx="15" cy="13" r="2" fill="var(--teal)"/></svg></span><span class="lab">Address :</span><b>Lorem ipsum dolor sit amet, sectetuer adipiscing&nbsp; 20165</b></div>
    <div class="row" style="left:19px;top:88px;width:242px"><span class="sq"><svg width="30" height="30"><rect width="30" height="30" fill="var(--green)"/><path d="M14 5h2v20h-2zM8 9h14l2 2-2 2H8zM22 15H8l-2 2 2 2h14z" fill="#fff"/></svg></span><span class="lab">City :</span><b>Consectetuer elit</b></div>
    <div class="row" style="left:289px;top:88px;width:236px"><span class="sq"><svg width="30" height="30"><rect width="30" height="30" fill="var(--orange)"/><path d="M6 12l9-6 9 6v11H6z" fill="#fff"/><path d="M6 12l9 7 9-7" fill="none" stroke="var(--orange)" stroke-width="1.5"/></svg></span><span class="lab">Zip :</span><b>elit20165</b></div>
    <div class="row" style="left:19px;top:128px;width:242px"><span class="sq"><svg width="30" height="30"><rect width="30" height="30" fill="var(--yellow)"/><rect x="10" y="5" width="10" height="20" rx="2" fill="#fff"/><rect x="12" y="8" width="6" height="12" fill="var(--yellow)"/></svg></span><span class="lab">Phone :</span><b>5550142873</b></div>
    <div class="row" style="left:289px;top:128px;width:236px"><span class="sq"><svg width="30" height="30"><rect width="30" height="30" fill="var(--teal)"/><path d="M9 6l4 4-2 3c1 3 3 5 6 6l3-2 4 4-3 3C12 24 6 18 6 9z" fill="#fff"/></svg></span><span class="lab">Cell Phone :</span><b>555 019284</b></div>
    <div class="row" style="left:19px;top:168px;width:506px"><span class="sq"><svg width="30" height="30"><rect width="30" height="30" fill="var(--blue)"/><rect x="6" y="9" width="18" height="12" fill="#fff"/><path d="M6 9l9 7 9-7" fill="none" stroke="var(--blue)" stroke-width="1.5"/></svg></span><span class="lab">Email :</span><b>info@example.com</b></div>
  </section>

  <section class="abs card cal">
    <div class="cal-head"><span class="sq"><svg width="20" height="20"><rect x="1" y="3" width="18" height="16" fill="none" stroke="#fff" stroke-width="2"/><path d="M5 1v4M15 1v4" stroke="#fff" stroke-width="2"/><path d="M4 9h2v2H4zM8 9h2v2H8zM12 9h2v2h-2zM4 13h2v2H4zM8 13h2v2H8zM12 13h2v2h-2z" fill="#fff"/></svg></span>Calendar</div>
    <span class="dow" style="left:8px">Su</span><span class="dow" style="left:47px">Mo</span><span class="dow" style="left:87px">Tu</span><span class="dow" style="left:127px">We</span><span class="dow" style="left:167px">Th</span><span class="dow" style="left:207px">Fr</span><span class="dow" style="left:247px">Sa</span>
    <span class="day" style="left:169px;top:84px">1</span><span class="day" style="left:209px;top:84px">2</span><span class="day" style="left:249px;top:84px">3</span>
    <span class="day sun" style="left:10px;top:124px">4</span><span class="day" style="left:49px;top:124px">5</span><span class="day" style="left:89px;top:124px">6</span><span class="day" style="left:129px;top:124px">7</span><span class="day" style="left:169px;top:124px">8</span><span class="day" style="left:209px;top:124px">9</span><span class="day" style="left:249px;top:124px">10</span>
    <span class="day sun" style="left:10px;top:164px">11</span><span class="day" style="left:49px;top:164px">12</span><span class="day today" style="left:89px;top:164px">13</span><span class="day" style="left:129px;top:164px">14</span><span class="day" style="left:169px;top:164px">15</span><span class="day" style="left:209px;top:164px">16</span><span class="day" style="left:249px;top:164px">17</span>
    <span class="day sun" style="left:10px;top:204px">18</span><span class="day" style="left:49px;top:204px">19</span><span class="day" style="left:89px;top:204px">20</span><span class="day" style="left:129px;top:204px">21</span><span class="day" style="left:169px;top:204px">22</span><span class="day" style="left:209px;top:204px">23</span><span class="day" style="left:249px;top:204px">24</span>
    <span class="day sun" style="left:10px;top:244px">25</span><span class="day" style="left:49px;top:244px">26</span><span class="day" style="left:89px;top:244px">27</span><span class="day" style="left:129px;top:244px">28</span><span class="day" style="left:169px;top:244px">29</span><span class="day" style="left:209px;top:244px">30</span><span class="day" style="left:249px;top:244px"></span>
  </section>

  <section class="abs card msg" style="left:365px">
    <div class="msg-head"><span class="sq" style="background:var(--green)"><svg width="22" height="20"><rect x="1" y="1" width="14" height="10" rx="2" fill="#fff"/><path d="M4 11v4l4-4z" fill="#fff"/><rect x="8" y="7" width="13" height="9" rx="2" fill="#fff" stroke="var(--green)"/></svg></span>Emloyess Secial Message</div>
    <p><span class="q">“</span> Lorem ipsum dolor amet, consectetuer adipiscing elit, sed diam nonummy nibh euis mod tincidunt ut laoreet dolore ma gna aliquam erat volutpat. Ut wisi enim ad , <span class="q">”</span></p>
  </section>
  <section class="abs card msg" style="left:647px">
    <div class="msg-head"><span class="sq" style="background:var(--yellow)"><svg width="22" height="20"><rect x="1" y="1" width="14" height="10" rx="2" fill="#fff"/><path d="M4 11v4l4-4z" fill="#fff"/><rect x="8" y="7" width="13" height="9" rx="2" fill="#fff" stroke="var(--yellow)"/></svg></span>Company Secial Message</div>
    <p><span class="q">“</span> Lorem ipsum dolor amet, consectetuer adipiscing elit, sed diam nonummy nibh euis mod tincidunt ut laoreet dolore ma gna aliquam erat volutpat. Ut wisi enim ad , <span class="q">”</span></p>
  </section>

  <a class="abs btn" style="left:365px;top:798px;width:263px;background:var(--blue)"><span class="ic" style="background:var(--blue-d)"><svg width="40" height="40"><path d="M33 20a13 13 0 1 1-4-9.5" fill="none" stroke="#fff" stroke-width="5"/><path d="M24 4h12v12z" fill="#fff"/></svg></span>Re-Hire</a>
  <a class="abs btn" style="left:647px;top:798px;width:263px;background:var(--orange)"><span class="ic" style="background:var(--orange-d)"><svg width="40" height="40"><path d="M30 11a13 13 0 1 0 0 18" fill="none" stroke="#fff" stroke-width="5"/><path d="M16 18h14v-5l8 7-8 7v-5H16z" fill="#fff"/></svg></span>Terminate</a>

  <a class="abs btn" style="left:929px;top:503px;width:295px;background:var(--orange)"><span class="ic" style="background:var(--orange-d)"><svg width="34" height="34"><path d="M6 8l10-6 10 6-10 6z" fill="#fff"/><rect x="3" y="18" width="24" height="13" rx="2" fill="#fff"/><text x="15" y="29" font-size="11" font-weight="700" fill="var(--orange-d)" text-anchor="middle" font-family="Lato,sans-serif">$</text></svg></span>Direct Deposit</a>
  <a class="abs btn" style="left:929px;top:576px;width:295px;background:var(--green)"><span class="ic" style="background:var(--green-d)"><svg width="30" height="40"><circle cx="17" cy="6" r="5" fill="#fff"/><path d="M8 16h12l-4 18h6v4H6l4-18H7z" fill="#fff"/></svg></span>Information Change</a>
  <a class="abs btn" style="left:929px;top:649px;width:295px;background:var(--yellow)"><span class="ic" style="background:var(--yellow-d)"><svg width="42" height="42"><path d="M8 21a14 14 0 1 0 4-10" fill="none" stroke="#fff" stroke-width="4"/><path d="M4 9l9 0-2 9z" fill="#fff"/><path d="M22 12v10l6 4" fill="none" stroke="#fff" stroke-width="3.5"/></svg></span>Time Off Request</a>
  <a class="abs btn" style="left:929px;top:722px;width:295px;background:var(--blue)"><span class="ic" style="background:var(--blue-d)"><svg width="38" height="34"><rect x="2" y="14" width="32" height="18" rx="2" fill="none" stroke="#fff" stroke-width="3"/><path d="M8 26h10" stroke="#fff" stroke-width="3"/><path d="M20 22l14-18 3 3-14 17h-4z" fill="#fff"/></svg></span>Paystubs</a>
  <a class="abs btn" style="left:929px;top:795px;width:295px;background:var(--dark)"><span class="ic" style="background:var(--dark-d)"><svg width="34" height="30"><rect x="11" y="2" width="12" height="6" rx="2" fill="none" stroke="#fff" stroke-width="3"/><rect x="2" y="7" width="30" height="21" rx="3" fill="#fff"/><path d="M14 12h6v4h4v6h-4v4h-6v-4h-4v-6h4z" fill="var(--dark-d)"/></svg></span>Health Insurance</a>

  <footer class="abs footer">© 2016 Lumora.&nbsp; All Rights Reserved</footer>
</div>
</body>
</html>
```